Pine Hollow Canine Massage Needs a Business Card Design

Pine Hollow Canine Massage is a new therapeutic canine massage company located in Nederland, Colorado. I need a business card design that include my logo and basic contact information.

Target Market(s)

Pet owners, veterinarians

Industry/Entity Type

Business

Contact Information for Business Card

Linda Morrow, CCMT
303.518.7290
linda@pinehollowmassage.example
www.pinehollowmassage.example

Colors
6c459b
886aae
b8a6cd
a64599
b768aa
d3a5cc
fbed22

Requirements
Must have
• Font should be similar to font in logo.

```html
<!DOCTYPE html>
<html lang="en">
<head>
<meta charset="utf-8">
<title>Pine Hollow Canine Massage — Business Card</title>
<link rel="stylesheet" href="https://fonts.googleapis.com/css2?family=Open+Sans:wght@400;600;700&display=swap">
<style>
  :root {
    --purple-deep: #6c459b;
    --purple-mid: #886aae;
    --lavender: #b8a6cd;
    --lime: #d8dc2c;
    --card-white: #f7f7f6;
    --ink: #3b3340;
    --backdrop: #e9e6e1;
  }
  * { margin: 0; padding: 0; box-sizing: border-box; }
  html, body {
    width: 1200px; height: 1022px; overflow: hidden;
    background: var(--backdrop);
    font-family: "Open Sans", Arial, sans-serif;
  }
  .card {
    position: absolute; left: 150px; top: 254px;
    width: 900px; height: 514px;
    background: var(--card-white);
    border-radius: 22px;
    overflow: hidden;
    box-shadow: 0 10px 30px rgba(60, 45, 30, 0.25);
  }
  .card-bands { position: absolute; inset: 0; }
  .holder { position: absolute; left: 300px; top: 72px; display: flex; align-items: flex-start; gap: 8px; }
  .holder-name {
    font-size: 42px; font-weight: 700; color: var(--purple-deep);
    letter-spacing: 0.5px; line-height: 1;
  }
  .holder-title {
    font-size: 17px; font-weight: 400; color: var(--lavender);
    letter-spacing: 1px; line-height: 1; margin-top: -8px;
  }
  .contact {
    position: absolute; right: 46px; top: 268px;
    list-style: none; text-align: right; color: var(--ink);
  }
  .contact li {
    display: flex; justify-content: flex-end; align-items: center;
    gap: 10px; font-size: 17px; line-height: 34px;
  }
  .contact .phone { font-size: 21px; margin-bottom: 10px; }
  .contact svg { width: 14px; height: 14px; flex: none; }
  .brand {
    position: absolute; left: 40px; bottom: 40px;
    display: flex; align-items: center; gap: 16px;
  }
  .brand-dot {
    width: 96px; height: 96px; border-radius: 50%;
    background: var(--lavender);
  }
  .brand-name {
    font-size: 18px; font-weight: 700; color: var(--purple-deep);
    line-height: 1.3; text-transform: uppercase; letter-spacing: 1px;
  }
</style>
</head>
<body>
  <article class="card">
    <svg class="card-bands" viewBox="0 0 900 514" width="900" height="514" aria-hidden="true">
      <path d="M420 514 C480 320 620 150 900 80 L900 514 Z" fill="var(--lime)"/>
      <path d="M392 514 C452 318 598 140 880 66 C604 150 468 322 408 514 Z" fill="var(--purple-deep)"/>
    </svg>

    <header class="holder">
      <h1 class="holder-name">Linda Morrow</h1>
      <span class="holder-title">CCMT</span>
    </header>

    <ul class="contact">
      <li class="phone">303.518.7290
        <svg viewBox="0 0 14 14"><rect x="3" y="1" width="8" height="12" rx="1.5" fill="none" stroke="var(--purple-mid)" stroke-width="1.4"/></svg>
      </li>
      <li>linda@pinehollowmassage.example
        <svg viewBox="0 0 14 14"><rect x="1" y="3" width="12" height="8" rx="1" fill="none" stroke="var(--purple-mid)" stroke-width="1.4"/><path d="M1 3 L7 8 L13 3" fill="none" stroke="var(--purple-mid)" stroke-width="1.2"/></svg>
      </li>
      <li>www.pinehollowmassage.example
        <svg viewBox="0 0 14 14"><circle cx="7" cy="7" r="5.5" fill="none" stroke="var(--purple-mid)" stroke-width="1.4"/><path d="M1.5 7 H12.5 M7 1.5 C4 5 4 9 7 12.5 M7 1.5 C10 5 10 9 7 12.5" fill="none" stroke="var(--purple-mid)" stroke-width="1"/></svg>
      </li>
    </ul>

    <div class="brand">
      <span class="brand-dot"></span>
      <p class="brand-name">Pine Hollow<br>Canine Massage</p>
    </div>
  </article>
</body>
</html>
```